Business Card Design for Small Electrical Contractor

I need to update my business card into something a little more modern. We are a small electrical contracting company. We service domestic and commercial places around Sydney. We have 2 logo designs at the moment. I have uploaded both and 2 different sizes to work with.

Industry/Entity Type

Business

Contact Information for Business Card

Ted Corbin
8/21-23 Holt St, Fernhaven 2087
t - (02) 9471 3820
m - 0427 915 304
E - info@corbinelec.example.au
W - corbinelec.example.au
ABN: 42 907 518 263

Font styles to use
Sans Serif

Requirements
Must have
• I would also like to see the below fit on somewhere aswell
• - Licensed Electrician
• - Level 2 (Cat 1 & 4)
• - Domestic
• - Commercial
• - Repairs and Installations
• - Data
Nice to have
• Try and keep similar colours as logo
Should not have
• No lightning bolts or light globes. Smart and professional please.

```html
<!DOCTYPE html>
<html lang="en">
<head>
<meta charset="utf-8">
<title>Corbin Electrical – Business Card</title>
<link href="https://fonts.googleapis.com/css2?family=Open+Sans:wght@400;600;700&display=swap" rel="stylesheet">
<style>
  :root {
    --backdrop: #2a2c30;
    --forest: #0f3a36;
    --amber: #f39a1e;
    --paper: #ffffff;
    --ink: #1a1a1a;
    --ink-green: #123f3a;
  }
  * { box-sizing: border-box; margin: 0; padding: 0; }
  html, body { width: 1200px; height: 864px; overflow: hidden; }
  body {
    background: var(--backdrop);
    font-family: "Open Sans", sans-serif;
    display: flex;
    flex-direction: column;
    align-items: center;
    justify-content: center;
    gap: 56px;
  }
  .card {
    position: relative;
    width: 540px;
    height: 330px;
    border-radius: 3px;
  }
  .card--back { background: var(--forest); color: var(--paper); }
  .card--front { background: var(--paper); color: var(--ink); }

  .brand {
    position: absolute;
    top: 42px;
    right: 40px;
    display: flex;
    align-items: center;
    gap: 10px;
  }
  .brand__dot {
    width: 12px; height: 12px;
    border-radius: 50%;
    background: var(--amber);
  }
  .brand__name {
    font-weight: 600;
    font-size: 30px;
    letter-spacing: 0.5px;
  }
  .card--back .brand__name { color: var(--paper); }
  .card--front .brand__name { color: var(--ink-green); }
  .brand__rule {
    position: absolute;
    top: 92px;
    right: 40px;
    width: 300px;
    height: 1.5px;
    background: var(--amber);
  }

  .services {
    position: absolute;
    left: 44px;
    top: 138px;
    list-style: none;
    font-size: 14px;
    font-weight: 600;
    line-height: 25px;
  }
  .services li { display: flex; align-items: center; gap: 10px; }
  .services li::before {
    content: "";
    width: 7px; height: 7px;
    border-radius: 50%;
    background: var(--amber);
  }

  .person {
    position: absolute;
    left: 44px;
    top: 132px;
    font-size: 14px;
    line-height: 21px;
  }
  .person__name {
    font-size: 19px;
    font-weight: 700;
    color: var(--ink-green);
    line-height: 26px;
  }

  .contacts {
    position: absolute;
    right: 40px;
    bottom: 34px;
    list-style: none;
    font-size: 14.5px;
    line-height: 26px;
    text-align: right;
  }
  .contacts li { display: flex; justify-content: flex-end; align-items: center; gap: 8px; }
  .contacts svg { width: 12px; height: 12px; fill: var(--ink-green); flex: none; }
</style>
</head>
<body>

<section class="card card--back" aria-label="Card back">
  <div class="brand">
    <span class="brand__dot"></span>
    <span class="brand__name">Corbin Electrical</span>
  </div>
  <div class="brand__rule"></div>
  <ul class="services">
    <li>Domestic</li>
    <li>Commercial</li>
    <li>Repairs and Installations</li>
    <li>Data</li>
  </ul>
</section>

<section class="card card--front" aria-label="Card front">
  <div class="brand">
    <span class="brand__dot"></span>
    <span class="brand__name">Corbin Electrical</span>
  </div>
  <div class="brand__rule"></div>

  <div class="person">
    <p class="person__name">Ted Corbin</p>
    <p>Licensed Electrician</p>
    <p>Level 2 (Cat 1 &amp; 4)</p>
    <p>ABN: 42 907 518 263</p>
  </div>

  <ul class="contacts">
    <li>(02) 9471 3820
      <svg viewBox="0 0 24 24" aria-hidden="true"><path d="M6.6 10.8a15.1 15.1 0 0 0 6.6 6.6l2.2-2.2a1 1 0 0 1 1-.25 11.4 11.4 0 0 0 3.6.57 1 1 0 0 1 1 1V20a1 1 0 0 1-1 1A17 17 0 0 1 3 4a1 1 0 0 1 1-1h3.5a1 1 0 0 1 1 1c0 1.25.2 2.450.57 3.57a1 1 0 0 1-.25 1z"/></svg>
    </li>
    <li>0427 915 304
      <svg viewBox="0 0 24 24" aria-hidden="true"><path d="M7 1h10a2 2 0 0 1 2 2v18a2 2 0 0 1-2 2H7a2 2 0 0 1-2-2V3a2 2 0 0 1 2-2zm0 3v14h10V4zm5 15.5a1 1 0 1 0 0 2 1 1 0 0 0 0-2z"/></svg>
    </li>
    <li>info@corbinelec.example.au
      <svg viewBox="0 0 24 24" aria-hidden="true"><path d="M2 5h20v14H2zm2 2v.5l8 5 8-5V7l-8 5z"/></svg>
    </li>
    <li>corbinelec.example.au
      <svg viewBox="0 0 24 24" aria-hidden="true"><path d="M12 2a10 10 0 1 0 0 20 10 10 0 0 0 0-20zm0 2c1 0 2.3 2 2.8 5H9.2C9.7 6 11 4 12 4zM4.3 11h3.7a20 20 0 0 0 .2 2H4.3a8 8 0 0 1 0-2zm11.7 0h3.7a8 8 0 0 1 0 2H16a20 20 0 0 0 0-2zm-6.8 4h5.6c-.5 3-1.8 5-2.8 5s-2.3-2-2.8-5z"/></svg>
    </li>
    <li>8/21-23 Holt St, Fernhaven 2087
      <svg viewBox="0 0 24 24" aria-hidden="true"><path d="M12 2a7 7 0 0 0-7 7c0 5 7 13 7 13s7-8 7-13a7 7 0 0 0-7-7zm0 9.5a2.5 2.5 0 1 1 0-5 2.5 2.5 0 0 1 0 5z"/></svg>
    </li>
  </ul>
</section>

</body>
</html>
```